Design a styled business card for an intimacy and attachment psychologist

I am a Psychologist providing online therapy to patients across the United States. My work is interpersonal and emotion-focused, with an emphasis on the client-therapist relationship. My primary areas of work are very personal, including sexuality and gender, abuse and trauma, and grief and loss. My target audience will be adults of all ages 18+.
My business card should convey a warm and inviting feeling of professionalism that is also casual and comfortable.
The front should be fairly simple and professional, consisting of:
- My name, Dr. Rosalind Petrakis
- My title, Licensed Psycholigist
- My logo
On either the front or the back, my contact information should be listed:
- ros@drrospetrakis.example
- 555.014.7788
- drrospetrakis.example
On the rear, I would like a description of the areas that I specialize in. This can be formatted in any way that appears stylistically interesting.
Individual and Couples
Relationships and Infidelity
Sexual Health & Aging
Gender Identity & Sexual Orientation
Abuse and Trauma
Sexual Compulsivity & Addiction
Sexual Dysfunction
Target Market(s)
My target audience will be adults of all ages 18+.
Industry/Entity Type
Psychology
Contact Information for Business Card
The front should be fairly simple and professional, consisting of: - My name, Dr. Rosalind Petrakis - My title, Licensed Psycholigist - My logo On either the front or the back, my contact information should be listed: - ros@drrospetrakis.example - 555.014.7788 - drrospetrakis.example On the rear, I would like a description of the areas that I specialize in. This can be formatted in any way that appears stylistically interesting. Individual and Couples Relationships and Infidelity Sexual Health & Aging Gender Identity & Sexual Orientation Abuse and Trauma Sexual Compulsivity & Addiction Sexual Dysfunction
- Follow brand guide

```html
<!DOCTYPE html>
<html lang="en">
<head>
<meta charset="utf-8">
<title>Dr. Rosalind Petrakis — Business Card</title>
<link rel="stylesheet" href="https://fonts.googleapis.com/css2?family=Arimo:wght@400;700&display=swap">
<style>
  :root {
    --bg: #2b2b2d;
    --plum: #2f2656;
    --plum-light: #3d3468;
    --navy: #2a2547;
    --coral: #ee3d40;
    --ink: #3a3650;
    --white: #ffffff;
    --white-soft: rgba(255,255,255,.78);
    --teal: #5fd0b4;
  }
  * { box-sizing: border-box; margin: 0; padding: 0; }
  html, body { width: 1200px; height: 900px; overflow: hidden; background: var(--bg); }
  body { font-family: "Arimo", sans-serif; }
  .canvas { position: relative; width: 1200px; height: 900px; }

  .card {
    position: absolute; left: 250px; width: 700px; height: 400px;
    border-radius: 10px; overflow: hidden;
    box-shadow: 0 10px 30px rgba(0,0,0,.35);
  }
  .card--front { top: 40px; background: linear-gradient(135deg, var(--plum) 0%, var(--plum) 55%, var(--plum-light) 100%); }
  .card--back { top: 460px; background: var(--white); }

  /* Front */
  .front__circle {
    position: absolute; left: 200px; top: 50px; width: 300px; height: 300px;
    border-radius: 50%; background: rgba(255,255,255,.06);
  }
  .front__name {
    position: absolute; left: 0; right: 0; top: 118px; text-align: center;
    color: var(--white); font-weight: 700; font-size: 52px; line-height: 1.1;
  }
  .specialties {
    position: absolute; left: 60px; right: 60px; top: 290px;
    list-style: none; text-align: center;
    color: var(--white-soft); font-size: 14px; line-height: 1.9;
  }
  .specialties__item { display: inline; }
  .specialties__item + .specialties__item::before { content: "•"; margin: 0 10px; color: var(--teal); }

  /* Back */
  .brand { position: absolute; right: 50px; top: 56px; display: flex; align-items: center; gap: 22px; }
  .brand__dot { width: 96px; height: 96px; border-radius: 50%; background: var(--teal); flex: none; }
  .brand__name { color: var(--navy); font-weight: 700; font-size: 34px; line-height: 1.1; }

  .identity { position: absolute; left: 56px; top: 190px; }
  .identity__name { color: var(--coral); font-weight: 700; font-size: 28px; line-height: 1.2; }
  .identity__title { color: var(--ink); font-size: 20px; margin-top: 2px; }
  .divider { position: absolute; left: 50px; right: 50px; top: 262px; height: 2px; background: var(--navy); }

  .contact { position: absolute; left: 56px; top: 280px; list-style: none; font-size: 22px; color: var(--ink); }
  .contact__item { display: flex; align-items: center; gap: 12px; margin-bottom: 8px; }
  .contact__icon { width: 20px; height: 20px; flex: none; }

  .website { position: absolute; right: 50px; bottom: 24px; font-weight: 700; font-size: 22px; color: var(--navy); }
  .website__domain { color: var(--coral); }
</style>
</head>
<body>
<main class="canvas">
  <section class="card card--front">
    <div class="front__circle" aria-hidden="true"></div>
    <p class="front__name">Dr. Rosalind<br>Petrakis</p>
    <ul class="specialties">
      <li class="specialties__item">Individual and Couples</li>
      <li class="specialties__item">Relationships and Infidelity</li>
      <li class="specialties__item">Sexual Health &amp; Aging</li>
      <li class="specialties__item">Gender Identity &amp; Sexual Orientation</li>
      <li class="specialties__item">Abuse and Trauma</li>
      <li class="specialties__item">Sexual Compulsivity &amp; Addiction</li>
      <li class="specialties__item">Sexual Dysfunction</li>
    </ul>
  </section>

  <section class="card card--back">
    <div class="brand">
      <div class="brand__dot" aria-hidden="true"></div>
      <p class="brand__name">Dr. Rosalind<br>Petrakis</p>
    </div>

    <div class="identity">
      <h1 class="identity__name">Dr. Rosalind Petrakis</h1>
      <p class="identity__title">Licensed Psycholigist</p>
    </div>
    <div class="divider"></div>

    <ul class="contact">
      <li class="contact__item">
        <svg class="contact__icon" viewBox="0 0 24 24" fill="none" stroke="#ee3d40" stroke-width="2" stroke-linecap="round" stroke-linejoin="round"><path d="M5 3h4l2 5-2.5 1.5a11 11 0 0 0 6 6L16 13l5 2v4a2 2 0 0 1-2 2A16 16 0 0 1 3 5a2 2 0 0 1 2-2z"/></svg>
        555.014.7788
      </li>
      <li class="contact__item">
        <svg class="contact__icon" viewBox="0 0 24 24" fill="none" stroke="#ee3d40" stroke-width="2" stroke-linejoin="round"><rect x="3" y="5" width="18" height="14" rx="1"/><path d="M3 6l9 7 9-7"/></svg>
        ros@drrospetrakis.example
      </li>
    </ul>

    <p class="website">www.<span class="website__domain">drrospetrakis</span>.example</p>
  </section>
</main>
</body>
</html>
```